Aquatic View

We need a web design for a new window cleaning company name Bright Pane Services. We are located in Grand Cayman, Cayman Islands. We are a small company, a team of husband and wife. Our services include residencial interior and exterior window cleaning and commercial. Extra services such as ceiling fans cleaning, mirrors, high dusting. Home cleaning services. Power washing. Explaining the service. We want a modern, beachy style with aquatic colors. We want to use our domain name "brightpaneservices.ky". We want to portray a clean, modern and professional design.

Target Market(s)

Big Home owners

Industry/Entity Type

Cleaning Service

Contact Information for Business Card

Company Name: Bright Pane Services
Name: Gerald Thornbury owner/manager
Phone: 345-9418372
Email: gerald@brightpaneservices.ky
Website: brightpaneservices.ky
Address: P.O.Box 2846 GT, George Town, Grand Cayman KY1-1304 Cayman Islands

Number of Pages Required

2 page

Font styles to use
Sans Serif

Colors
0592cd
0455a3
33a6d7
85cae6
cadf82
abd036
fbf289

Requirements
Nice to have
• Pictures of an ocean view and palm trees from clear windows.
• https://quotrelvane.com/estimately/
• Use the above for "free estimate".

```html
<!DOCTYPE html>
<html lang="en">
<head>
<meta charset="utf-8">
<title>Bright Pane Services</title>
<link href="https://fonts.googleapis.com/css2?family=Open+Sans:wght@300;400;600;700&display=swap" rel="stylesheet">
<style>
:root{
  --green:#8cc414;
  --blue-top:#3a87c8;
  --footer:#3f86c9;
  --footer-line:#5a97d2;
  --text:#777;
  --white:#fff;
  --border:#e6e6e6;
  --brand:#1f4f8a;
}
*{margin:0;padding:0;box-sizing:border-box}
html,body{width:684px;height:1200px;overflow:hidden;background:var(--white)}
body{position:relative;font-family:"Open Sans",Arial,sans-serif;color:var(--text)}
.abs{position:absolute}
.btn{position:absolute;background:var(--green);color:var(--white);font-size:8.5px;display:flex;align-items:center;justify-content:center;text-decoration:none}

.top-rule{left:0;top:0;width:684px;height:2px;background:var(--blue-top)}
.call-pill{left:500px;top:0;width:126px;height:29px;background:var(--blue-top);border-radius:0 0 12px 12px;color:var(--white);display:flex;align-items:center;justify-content:center;gap:4px}
.call-pill small{font-size:5.5px}
.call-pill span{font-size:8.5px}
.brand{left:57px;top:42px;display:flex;align-items:center;gap:5px;color:var(--brand);font-weight:700;font-size:7.5px;line-height:1.05}
.brand i{width:12px;height:12px;border-radius:50%;background:var(--blue-top);display:block}
.nav-link{position:absolute;top:39px;height:25px;font-size:6.6px;color:#444;text-decoration:none;display:flex;align-items:center}
.nav-link.active{background:var(--green);color:var(--white);left:241px;width:63px;justify-content:center}
.header-rule{left:0;top:81px;width:684px;height:1px;background:var(--green)}

.hero-photo{left:0;top:82px;width:684px;height:294px;background:linear-gradient(180deg,#3d8fd0 0%,#6fb9e2 30%,#5cc8dc 48%,#2fbac8 65%,#1ea2b2 85%,#15808e 100%)}
.hero-title{left:56px;top:166px;font-size:21px;font-weight:700;color:var(--white);letter-spacing:.3px}
.hero-sub{left:56px;top:198px;font-size:14.5px;font-weight:300;color:var(--white);letter-spacing:.2px}
.hero-btn{left:56px;top:234px;width:82px;height:25px;font-weight:600}
.slide-arrow{top:195px;width:29px;height:29px;border-radius:50%;background:rgba(255,255,255,.25)}

.welcome-title{left:56px;top:396px;font-size:15px;font-weight:700;color:var(--green)}
.welcome-text{left:56px;width:400px;font-size:6.3px;line-height:11.5px;color:var(--text)}
.welcome-btn{left:56px;top:506px;width:70px;height:23px}
.welcome-photo{left:472px;top:397px;width:154px;height:128px;background:var(--white);box-shadow:0 1px 4px rgba(0,0,0,.3);padding:4px}
.welcome-photo div{width:100%;height:100%;background:linear-gradient(180deg,#c9ddd6 0%,#b5ccc6 60%,#cdb597 75%,#b89a78 100%)}
.section-rule{left:0;top:554px;width:684px;height:1px;background:#eee}

.services-title{left:56px;top:565px;font-size:14px;font-weight:700;color:var(--green)}
.carousel-nav{left:601px;top:568px;width:26px;height:26px;border-radius:50%;border:1px solid #ddd;display:flex;align-items:center;justify-content:center}
.card{position:absolute;top:602px;width:139px;height:204px;border:1px solid var(--border);background:var(--white)}
.card .shot{position:absolute;left:4px;top:4px;width:129px;height:91px}
.card h3{position:absolute;left:11px;top:103px;font-size:12.3px;font-weight:400;color:var(--green);white-space:nowrap}
.card p{position:absolute;left:12px;top:127px;width:120px;font-size:6.2px;line-height:11px}
.card .btn{left:12px;top:168px;width:67px;height:19px;font-size:8px}

.banner-photo{left:0;top:827px;width:684px;height:193px;background:linear-gradient(180deg,#5fb4ea 0%,#8fd0f2 42%,#3a8fc9 58%,#8fb3c8 75%,#c9ccc8 88%,#6b7278 100%)}
.banner-text{left:70px;top:862px;width:240px;font-size:17px;line-height:23px;color:var(--white);text-shadow:0 1px 3px rgba(0,0,0,.6)}
.banner-btn{left:70px;top:965px;width:102px;height:30px;font-size:11px;letter-spacing:.3px}

.footer-bg{left:0;top:1020px;width:684px;height:180px;background:var(--footer)}
.footer-head{top:1038px;font-size:7px;font-weight:700;display:flex;align-items:center;gap:5px;letter-spacing:.2px;color:var(--white)}
.footer-list{list-style:none;color:var(--white)}
.footer-list li{font-size:6.5px;height:16px}
.col-rule{top:1030px;width:1px;height:125px;background:var(--footer-line)}
.footer-note{left:166px;top:1060px;font-size:6.5px;color:var(--white)}
.email-field{left:166px;top:1080px;width:133px;height:20px;background:var(--white);font-size:5.5px;color:#888;display:flex;align-items:center;padding-left:7px}
.submit-btn{left:166px;top:1112px;width:70px;height:23px}
.social{top:1066px;width:20px;height:20px;border-radius:50%;border:1.5px solid var(--white)}
.contact-item{padding-left:11px;position:relative}
.contact-item svg{position:absolute;left:0}
.contact-item b{font-weight:600}
.bottom-rule{left:0;top:1160px;width:684px;height:1px;background:var(--footer-line)}
.copyright{left:0;top:1173px;width:684px;text-align:center;font-size:6.5px;color:var(--white)}
.page-code{left:649px;top:1173px;font-size:6px;color:var(--white)}
</style>
</head>
<body>

<header>
  <div class="abs top-rule"></div>
  <div class="abs call-pill"><small>CALL US FREE:</small><span>+00 (0) 12345678</span></div>
  <div class="abs brand"><i></i>BRIGHT PANE<br>SERVICES</div>
  <nav>
    <a class="nav-link active" href="#">HOME</a>
    <a class="nav-link" href="#" style="left:329px">ABOUT US</a>
    <a class="nav-link" href="#" style="left:409px">OUR SERVICES</a>
    <a class="nav-link" href="#" style="left:503px">PRODUCTS</a>
    <a class="nav-link" href="#" style="left:586px">CONTACT US</a>
  </nav>
  <div class="abs header-rule"></div>
</header>

<section>
  <div class="abs hero-photo" role="img" aria-label="Photo of a wooden pier over turquoise Caribbean sea"></div>
  <div class="abs slide-arrow" style="left:15px"></div>
  <div class="abs slide-arrow" style="left:637px"></div>
  <h1 class="abs hero-title">WE ARE BRIGHT PANE</h1>
  <div class="abs hero-sub">SERVICES IN CAYMAN ISLANDS</div>
  <a class="btn hero-btn" href="#">Read More &raquo;</a>
</section>

<section>
  <h2 class="abs welcome-title">Welcome to Bright Pane Services!</h2>
  <p class="abs welcome-text" style="top:424px">We are a small husband and wife team serving Grand Cayman with careful residential and commercial window cleaning, inside and out. Every pane is washed, detailed and dried by hand so your ocean views stay crystal clear all season long.</p>
  <p class="abs welcome-text" style="top:466px">We also offer high dusting, mirrors, ceiling fans and power washing, with honest prices and friendly service.</p>
  <a class="btn welcome-btn" href="#">Read More &raquo;</a>
  <div class="abs welcome-photo"><div role="img" aria-label="Photo of a floor mop on a wooden floor"></div></div>
</section>
<div class="abs section-rule"></div>

<section>
  <h2 class="abs services-title">Our Services</h2>
  <div class="abs carousel-nav"><svg width="10" height="8" viewBox="0 0 10 8"><path d="M3 1 0.8 4 3 7M7 1 9.2 4 7 7" fill="none" stroke="#333" stroke-width="1"/></svg></div>

  <div class="card" style="left:56px">
    <div class="shot" role="img" aria-label="Photo of tall clean windows facing a garden" style="background:linear-gradient(180deg,#e7d2b6 0%,#d9e6ef 40%,#7dbb5a 75%,#c9a883 100%)"></div>
    <h3>Window Cleaning</h3>
    <p>Streak free glass for homes and offices, inside and outside.</p>
    <a class="btn" href="#">View More &raquo;</a>
  </div>
  <div class="card" style="left:200px">
    <div class="shot" role="img" aria-label="Photo of a white ceiling fan under skylights" style="background:linear-gradient(180deg,#eef3f7 0%,#dfe9f1 60%,#b7d3ea 100%)"></div>
    <h3>Ceiling Fans Cleaning</h3>
    <p>Dust free blades and motors for cleaner air in every room.</p>
    <a class="btn" href="#">View More &raquo;</a>
  </div>
  <div class="card" style="left:345px">
    <div class="shot" role="img" aria-label="Photo of a bright bathroom with a sea view" style="background:linear-gradient(180deg,#cfe3ef 0%,#a9c9dc 45%,#e8e8e8 65%,#a37a55 100%)"></div>
    <h3>Mirrors Cleaning</h3>
    <p>Spotless mirrors and glass panels polished to a clear finish.</p>
    <a class="btn" href="#">View More &raquo;</a>
  </div>
  <div class="card" style="left:489px">
    <div class="shot" role="img" aria-label="Photo of a hand wiping a window with a blue cloth" style="background:linear-gradient(135deg,#b8d46a 0%,#9fc7d8 50%,#4f86c6 70%,#d9e3a0 100%)"></div>
    <h3>High Dusting</h3>
    <p>Safe cleaning of tall shelves, beams, vents and light fixtures.</p>
    <a class="btn" href="#">View More &raquo;</a>
  </div>
</section>

<section>
  <div class="abs banner-photo" role="img" aria-label="Photo of a living room with a white sofa and ocean view windows"></div>
  <p class="abs banner-text">Extra services such as ceiling fans cleaning, mirrors, high dusting. Home cleaning services. Power washing.</p>
  <a class="btn banner-btn" href="#">ABOUT US</a>
</section>

<footer>
  <div class="abs footer-bg"></div>

  <h4 class="abs footer-head" style="left:56px"><svg width="8" height="8" viewBox="0 0 8 8"><path d="M3 5 5 3M2.5 3.5 1.2 4.8a1.4 1.4 0 0 0 2 2L4.5 5.5M5.5 4.5 6.8 3.2a1.4 1.4 0 0 0-2-2L3.5 2.5" fill="none" stroke="#fff" stroke-width="1"/></svg>QUICK LINKS</h4>
  <ul class="abs footer-list" style="left:56px;top:1060px">
    <li>Home</li><li>About us</li><li>Our Services</li><li>Products</li><li>Contact us</li>
  </ul>
  <div class="abs col-rule" style="left:150px"></div>

  <h4 class="abs footer-head" style="left:166px"><svg width="9" height="7" viewBox="0 0 9 7"><rect width="9" height="7" fill="#fff"/><path d="M0 0 4.5 3.8 9 0" fill="none" stroke="#3f86c9" stroke-width="1"/></svg>NEWS LETTER SIGNUP</h4>
  <div class="abs footer-note">Sign-up to be notified about news</div>
  <div class="abs email-field">Enter Your Email</div>
  <a class="btn submit-btn" href="#">SUBMIT</a>
  <div class="abs col-rule" style="left:322px"></div>

  <h4 class="abs footer-head" style="left:343px"><svg width="10" height="8" viewBox="0 0 10 8"><path d="M6 1H1v6h6V5M5 4l4-3M6 1h3v3" fill="none" stroke="#fff" stroke-width="1.1"/></svg>FOLLOW US</h4>
  <div class="abs social" style="left:343px;background:#3b5a98"></div>
  <div class="abs social" style="left:367px;background:#2aa3dc"></div>
  <div class="abs social" style="left:391px;background:#c9302c"></div>
  <div class="abs social" style="left:415px;background:#d24a4a"></div>
  <div class="abs social" style="left:439px;background:#d98c1c"></div>
  <div class="abs col-rule" style="left:475px"></div>

  <h4 class="abs footer-head" style="left:491px"><svg width="11" height="8" viewBox="0 0 11 8"><path d="M1 3Q5.5-1 10 3L8.5 4 7 3V2H4v1L2.5 4ZM3 4h5l1 4H2Z" fill="#fff"/></svg>CONTACT US</h4>
  <ul class="abs footer-list" style="left:494px;top:1059px;width:170px">
    <li class="contact-item" style="height:32px;line-height:16px"><svg style="top:4px" width="5" height="7" viewBox="0 0 5 7"><path d="M2.5 7 0.4 3.2A2.3 2.3 0 1 1 4.6 3.2Z" fill="#fff"/></svg><b>Office:</b> No Street Address, City Address, State, Country.</li>
    <li class="contact-item"><svg style="top:1px;left:1px" width="4" height="7" viewBox="0 0 4 7"><rect width="4" height="7" rx="1" fill="#fff"/></svg><b>Mobile:</b> +00 (0) 12345678</li>
    <li class="contact-item"><svg style="top:1px" width="6" height="6" viewBox="0 0 6 6"><rect y="2" width="6" height="4" fill="#fff"/><rect x="1" width="4" height="2" fill="#fff"/></svg><b>Fax:</b> +00 (0) 12345678</li>
    <li class="contact-item"><svg style="top:2px" width="6" height="5" viewBox="0 0 6 5"><rect width="6" height="5" fill="#fff"/></svg><b>Mail:</b> Contact@domainname.com</li>
  </ul>

  <div class="abs bottom-rule"></div>
  <div class="abs copyright">BRIGHT PANE SERVICES. &copy; 2015 | Privacy Policy</div>
  <div class="abs page-code">C16</div>
</footer>

</body>
</html>
```